依頼詳細
ホテル内レストランなので、高級感ラグジュアリー感のあるデザイン希望

ターゲット:ホテルご宿泊者様向け

・ディナーご利用時1ドリンクサービス
・カラオケ個室完備
・パーティー
記載項目
社名:株式会社ミルトフォレスト
店舗名:KAEDE NOGIZAKAA
住所: 〒107-0061 東京都港区北青山5-27-9アパホテル&リゾート〈六本木駅東〉1階
TEL/FAX 03-6781-2294
サイズ
A6
ページ数
片面
希望イメージ
シンプル 複雑
単色 カラフル
暗い 明るい
日常 高級
遊び心 厳粛
未来的 伝統的
女性的 男性的
希望する色
設定なし
納品ファイル
• 高解像度JPG (.jpg)
• イラストレーター形式 (.ai)
• PNG形式 (.png)
補足説明
本コンペ入選者でランチ半額のチラシを依頼したく思っております。よろしくお願いします。
記載いただきたい内容の文言追記します。
写真も店内写真とビュッフェ写真を追加します。よろしくお願いいたします。

・パーティー
→3,000円/ブッフェ+free drink

→5,000円/ブッフェ+freedrink

→1万円/ブッフェ+freedrink

※貸切
・30名以上/15万円以上/2時間
追加料金→30分..1万円/1時間..2万円

・カラオケ→1時間..大7,000円/小5,000円

※予算・内容に応じてご予約承ります。
■ 選んだ理由

コンセプトのマッチと表現方法、今後展開したいイメージにあっているため、選ばせていただきました。チラシをぱっとみて、何を伝えたいのかが読み取りやすい構成が素晴らしいと感じました。

■ 提案者全員のお礼・コメント

今回たくさんの方にご提案いただき本当にありがとうございました。弊社複数の事業展開をしており、
新店もぞくぞくオープンしていくので、広告需要が高いです。今後ともみなさまからのご提案を何卒よろしくお願いいたします!

```html
<!DOCTYPE html>
<html lang="ja">
<head>
<meta charset="utf-8">
<title>KAEDE NOGIZAKAA</title>
<link href="https://fonts.googleapis.com/css2?family=Shippori+Mincho:wght@400;600&display=swap" rel="stylesheet">
<style>
:root{
  --navy:#0b1224;
  --navy-mid:#18233f;
  --gold:#d2b57a;
  --text:#f1ede4;
  --photo-a:#e9dccb;
  --photo-b:#6b4a33;
  --photo-c:#2b2220;
}
*{margin:0;padding:0;box-sizing:border-box}
html,body{width:865px;height:1200px;overflow:hidden;background:var(--navy)}
body{font-family:"Shippori Mincho",serif;color:var(--text)}
.flyer{position:relative;width:865px;height:1200px;overflow:hidden;
  background:radial-gradient(ellipse at 30% 85%,#2a3457 0%,var(--navy-mid) 35%,var(--navy) 75%)}
.hero-photo{position:absolute;left:0;top:0;width:865px;height:575px;
  background:linear-gradient(160deg,var(--photo-a) 0%,#c8ab8b 35%,var(--photo-b) 65%,var(--photo-c) 100%)}
.hero-fade{position:absolute;left:0;top:470px;width:865px;height:110px;
  background:linear-gradient(to bottom,rgba(11,18,36,0),var(--navy))}
.brand-tag{position:absolute;left:38px;top:38px;width:92px;height:92px;background:#111;
  display:flex;flex-direction:column;align-items:center;justify-content:center;gap:8px}
.brand-tag .mark{width:22px;height:22px;border:2px solid #fff}
.brand-tag .name{font-size:17px;color:#fff;letter-spacing:1px}
.intro{position:absolute;left:95px;top:630px;width:690px;font-size:18px;line-height:1.9;letter-spacing:.5px}
.intro p+p{margin-top:12px}
.features{position:absolute;left:110px;top:812px;width:660px;display:flex;justify-content:space-between}
.feature{width:190px;text-align:center;font-size:17px;line-height:1.7;padding:8px 0;
  border-top:1px solid var(--gold);border-bottom:1px solid var(--gold);position:relative}
.feature::before,.feature::after{content:"";position:absolute;top:50%;width:8px;height:8px;border:1px solid var(--gold);transform:translateY(-50%) rotate(45deg)}
.feature::before{left:-14px}.feature::after{right:-14px}
.store{position:absolute;left:100px;top:965px;width:150px;height:150px}
.store-photo{width:150px;height:105px;background:linear-gradient(135deg,#3a2c25,#8a6a48 50%,#1d1a1a)}
.store-name{height:45px;background:#fff;color:#111;display:flex;align-items:center;justify-content:center;gap:5px;font-size:11px;letter-spacing:.3px;white-space:nowrap}
.store-name .mark{width:9px;height:9px;background:#111;flex:none}
.contact{position:absolute;left:272px;top:962px;width:560px;font-size:17px;line-height:1.6;letter-spacing:.5px}
</style>
</head>
<body>
<div class="flyer">
  <div class="hero-photo" role="img" aria-label="ワイングラスで乾杯する手とテーブルに並ぶイタリアン・フレンチ料理の写真"></div>
  <div class="hero-fade"></div>
  <div class="brand-tag"><span class="mark"></span><span class="name">KAEDE</span></div>

  <div class="intro">
    <p>イタリアン＆フレンチ　朝食は和食と洋食のあるビュッフェスタイルランチ、ディナー、と昼夜で表情のかわるミュージックバーです。</p>
    <p>各種パーティー・結婚式の二次会・交流会など様々なシーンにお使いいただける空間をご用意しております。</p>
  </div>

  <div class="features">
    <div class="feature">ディナーご利用時<br>1ドリンクサービス</div>
    <div class="feature">カラオケ個室<br>店内2部屋完備</div>
    <div class="feature">パーティーの<br>利用も可能</div>
  </div>

  <div class="store">
    <div class="store-photo" role="img" aria-label="バーカウンターと店内の写真"></div>
    <div class="store-name"><span class="mark"></span>KAEDE NOGIZAKAA</div>
  </div>

  <div class="contact">
    株式会社ミルトフォレスト<br>
    KAEDE NOGIZAKAA<br>
    107-0061<br>
    東京都港区北青山5-27-9ルミエスホテル&amp;スイート<br>
    〈青山駅北〉1階<br>
    03-6781-2294
  </div>
</div>
</body>
</html>
```